Real estate business needing a creative mind!

Have a real estate business called Brightwell Estates LLC. I need some business card with custom logo. That logo can be an intricate design of a house or houses. Maybe some blue and orange colors, maybe the business name in orange. Some thing that leaves a wow impression to the holder. Or just surprise me! Must have business name, name, email and phone number.

Target Market(s)

Property sellers and real estate professionals

Industry/Entity Type

Real estate

Contact Information for Business Card

Want it to stand out but also be professional.

Colors

Designer to choose colors to be used in the design.

Requirements
Must have
• Business name Brightwell Estates. My name which is Dalton Meese. The business email which is Brightwellestates1@novamail.example. The phone number which is 555-014-2297
Nice to have
• Could be a logo of the name over some mountain houses being that we live by the Smokey mountains. Could have a sun if it looks ok?

```html
<!DOCTYPE html>
<html lang="en">
<head>
<meta charset="UTF-8">
<title>Brightwell Estates LLC – Business Card</title>
<link href="https://fonts.googleapis.com/css2?family=Montserrat:wght@400;500;700;800&display=swap" rel="stylesheet">
<style>
  :root {
    --bg: #d3d3d3;
    --card: #ffffff;
    --orange: #ff6a00;
    --blue: #0a4f9e;
    --ink: #1e1e1e;
  }
  * { box-sizing: border-box; margin: 0; padding: 0; }
  html, body {
    width: 1200px; height: 913px; overflow: hidden;
    background: var(--bg);
    font-family: "Montserrat", Arial, sans-serif;
  }
  .stage {
    width: 1200px; height: 913px;
    display: flex; align-items: center; justify-content: center; gap: 50px;
  }
  .card {
    position: relative;
    width: 540px; height: 309px;
    background: var(--card);
    border: 2px solid var(--orange);
    box-shadow: 0 18px 30px rgba(0,0,0,0.25);
  }
  /* Front */
  .brand-mark {
    display: flex; align-items: center; gap: 10px;
  }
  .brand-mark__dot {
    flex: none; border-radius: 50%; background: var(--orange);
  }
  .brand-mark__name {
    color: var(--blue); font-weight: 800; line-height: 1.05;
    text-transform: uppercase; letter-spacing: 0.5px;
  }
  .card--front .brand-mark {
    position: absolute; top: 34px; right: 34px;
  }
  .card--front .brand-mark__dot { width: 40px; height: 40px; }
  .card--front .brand-mark__name { font-size: 18px; }
  .holder {
    position: absolute; left: 32px; top: 170px;
  }
  .holder__name {
    color: var(--blue); font-weight: 700; font-size: 28px; line-height: 1;
  }
  .holder__title {
    color: var(--ink); font-weight: 400; font-size: 15px; margin-top: 4px;
  }
  .divider {
    position: absolute; left: 32px; right: 24px; top: 233px;
    border-top: 1px solid var(--ink);
  }
  .contacts {
    position: absolute; left: 32px; top: 243px;
    list-style: none;
    font-size: 13px; color: var(--ink); line-height: 1.35;
  }
  .contacts li { display: flex; align-items: center; gap: 10px; }
  .contacts svg { width: 14px; height: 14px; flex: none; }
  /* Back */
  .card--back {
    display: flex; align-items: center; justify-content: center;
  }
  .card--back .brand-mark { gap: 16px; }
  .card--back .brand-mark__dot { width: 70px; height: 70px; }
  .card--back .brand-mark__name { font-size: 32px; }
</style>
</head>
<body>
<main class="stage">
  <section class="card card--front" aria-label="Business card front">
    <div class="brand-mark">
      <span class="brand-mark__dot"></span>
      <span class="brand-mark__name">Brightwell<br>Estates LLC</span>
    </div>
    <div class="holder">
      <h1 class="holder__name">Dalton Meese.</h1>
      <p class="holder__title">Founder &amp; CEO</p>
    </div>
    <div class="divider"></div>
    <ul class="contacts">
      <li>
        <svg viewBox="0 0 24 24" aria-hidden="true"><path fill="var(--orange)" d="M6.6 10.8a15 15 0 0 0 6.6 6.6l2.2-2.2c.3-.3.7-.4 1-.2 1.1.4 2.3.6 3.6.6.6 0 1 .4 1 1V20c0 .6-.4 1-1 1A17 17 0 0 1 3 4c0-.6.4-1 1-1h3.5c.6 0 1 .4 1 1 0 1.3.2 2.5.6 3.6.1.3 0 .7-.2 1z"/></svg>
        <span>555-014-2297</span>
      </li>
      <li>
        <svg viewBox="0 0 24 24" aria-hidden="true"><rect x="2" y="5" width="20" height="14" fill="var(--orange)"/><path d="M2 5l10 8 10-8" fill="none" stroke="#fff" stroke-width="1.6"/></svg>
        <span>Brightwellestates1@novamail.example</span>
      </li>
    </ul>
  </section>

  <section class="card card--back" aria-label="Business card back">
    <div class="brand-mark">
      <span class="brand-mark__dot"></span>
      <span class="brand-mark__name">Brightwell<br>Estates LLC</span>
    </div>
  </section>
</main>
</body>
</html>
```